Specialized tax accounting firm needs letterhead design

We need a letterhead design for a professional services firm called R. Desmond Pell Inc. The firm is essentially a very specialized tax accounting firm - instead of serving the end consumer, we support other public accounting firms in the area of Canadian and U.S. tax advisory and compliance (i.e. they call us on tax issues too complex for the general practitioner. Our byline is "Tax Support Services for Public Accounting Firms". Our letterhead should utilize our logo and be based on colours present in our logo (see file attached). The final design needs to convey professionalism and trustworthiness (we're hired by accountants after all!) while being creative and eye-catching.

I've attached:
The font used in the logo
The logo itself in a variety of file formats
A single page showing the key firm information which should be appearing in the letterhead

Please note that there is much more leather background around the logo than needs to be incorporated in the letterhead.

Industry/Entity Type

Accounting

```html
<!DOCTYPE html>
<html lang="en">
<head>
<meta charset="utf-8">
<title>R. Desmond Pell Inc. — Letterhead</title>
<link href="https://fonts.googleapis.com/css2?family=Cinzel:wght@400&display=swap" rel="stylesheet">
<style>
  :root {
    --backdrop: #e4e4e6;
    --paper: #ffffff;
    --band-dark: #0e0e0e;
    --band-mid: #1c1c1c;
    --ink-light: #f2f2f2;
    --ink-soft: #c9c9c9;
    --accent-orange: #f0a020;
  }
  * { box-sizing: border-box; margin: 0; padding: 0; }
  html, body {
    width: 1200px;
    height: 1000px;
    overflow: hidden;
    background: var(--backdrop);
    font-family: "Cinzel", "Times New Roman", serif;
  }
  .letterhead {
    position: absolute;
    left: 237px;
    top: 30px;
    width: 726px;
    height: 940px;
    background: var(--paper);
    box-shadow: 0 2px 10px rgba(0,0,0,0.12);
  }
  .header-band {
    position: absolute;
    left: 0; top: 0;
    width: 100%;
    height: 150px;
    background: radial-gradient(ellipse at 40% 40%, var(--band-mid), var(--band-dark) 75%);
    display: flex;
    flex-direction: column;
    justify-content: center;
    padding-left: 44px;
  }
  .firm-name {
    color: var(--ink-light);
    font-size: 32px;
    font-weight: 400;
    letter-spacing: 2px;
    line-height: 1.1;
  }
  .firm-tagline {
    color: var(--ink-soft);
    font-size: 12px;
    letter-spacing: 1.5px;
    line-height: 1.2;
    margin-top: 12px;
  }
  .footer-band {
    position: absolute;
    left: 0;
    bottom: 20px;
    width: 100%;
    height: 62px;
    background: radial-gradient(ellipse at 60% 50%, var(--band-mid), var(--band-dark) 75%);
    color: var(--ink-light);
    display: flex;
    flex-direction: column;
    justify-content: center;
    align-items: flex-end;
    padding-right: 30px;
    font-size: 10px;
    letter-spacing: 0.6px;
    line-height: 1.7;
  }
  .contact-line { white-space: nowrap; }
  .contact-label {
    color: var(--accent-orange);
    margin-left: 10px;
  }
  .contact-label:first-child { margin-left: 0; }
</style>
</head>
<body>
  <main class="letterhead">
    <header class="header-band">
      <div class="firm-name">R. Desmond Pell Inc.</div>
      <div class="firm-tagline">Tax Support Services for Public Accounting Firms</div>
    </header>

    <footer class="footer-band">
      <div class="contact-line">18-410 Harlow Street, Kestrel Bay, Nova Scotia, Canada B2X 4K7</div>
      <div class="contact-line">
        <span class="contact-label">Phone:</span> 902.555.0148
        <span class="contact-label">Fax:</span> 902.555.0192
        <span class="contact-label">Email:</span> office@pelltax.example
        <span class="contact-label">Web:</span> www.pelltax.example
      </div>
    </footer>
  </main>
</body>
</html>
```